依頼詳細
RPE歯科クリニック~行きます訪問歯科・送迎歯科~
のパンフレットを作成依頼致します。

1.パンフレットに使用したいデータ等がございません。以前使用していたパンフレットをPDFで添付いたしますのでご確認ください。添付エクセルデータがございます。こちらを参考にA4両面に収めてレイアウトしてください。

2. パンフレットは以前のパンフレットの(ピンク×水色、ピンク、水色)を希望しております。

3.1枚目の車のロゴはないので、作成いただいてもフリー素材でも結構ですのでお願い致します。

4.MAPは、添付フィル≪MAP_image≫をご確認ください。

5.仕上がりはA4両面イラストレーターデザインを希望いたします。フルカラーでお願いします。
サイズ
A4
ページ数
4ページ
希望イメージ
シンプル 複雑
単色 カラフル
暗い 明るい
日常 高級
遊び心 厳粛
未来的 伝統的
女性的 男性的
希望する色
赤系、水色系
納品ファイル
• イラストレーター形式 (.ai)
補足説明
修正致します

1.添付エクセルデータがございます。→PDFデータの為、文字おこしお願い致します。
医院名
RPE歯科クリニック
~行きます訪問歯科・送迎歯科~
パンフレットのカテゴリになっておりますが、
A4サイズ両面のチラシ作成依頼になります。

よろしくお願いいたします。
コンペ当選者を確約に変更いたしましたのでよろしくお願いいたします。

色使いや、歯を使ったイラストの可愛さと、全体的に見やすくバランスが良かったです。

たくさんのご提案ありがとうございました。 慣れない依頼にご提案くださり感謝しています。 また、機会がありましたら是非ご協力ください。 ありがとうございました。

```html
<!DOCTYPE html>
<html lang="ja">
<head>
<meta charset="utf-8">
<title>RPE歯科医院 訪問・送迎歯科クリニック</title>
<link rel="stylesheet" href="https://fonts.googleapis.com/css2?family=M+PLUS+Rounded+1c:wght@400;500;700;800&family=Kosugi+Maru&display=swap">
<style>
:root{
  --teal:#2aa3b5;
  --teal-dark:#1f8797;
  --pink:#ea8aa8;
  --pink-soft:#fbe3ea;
  --sky:#dff2f8;
  --sky-line:#9fd6e6;
  --green:#8cc63f;
  --text:#4a4a4a;
  --paper:#ffffff;
}
*{margin:0;padding:0;box-sizing:border-box}
html,body{width:849px;height:1200px;overflow:hidden;background:var(--paper)}
body{font-family:"M PLUS Rounded 1c","Kosugi Maru",sans-serif;color:var(--text);position:relative}

.hero{position:absolute;left:0;top:0;width:849px;height:460px;
  background:linear-gradient(180deg,#ffffff 0%,#eef8fb 40%,#e4f3f6 75%,#ffffff 100%)}
.hero-trees{position:absolute;right:0;top:0;width:240px;height:190px;
  background:radial-gradient(ellipse at 70% 30%,#cfe8b0 0%,#e6f3d6 50%,rgba(255,255,255,0) 75%)}
.hero-land{position:absolute;left:0;top:280px;width:330px;height:170px;
  background:radial-gradient(ellipse at 40% 60%,#d8ecc3 0%,#e7f3dc 45%,rgba(255,255,255,0) 75%)}
.hero-van{position:absolute;left:270px;top:330px;width:350px;height:125px;border-radius:40px 60px 14px 14px;
  background:linear-gradient(180deg,#f4f6f7 0%,#dfe4e7 100%)}
.hero-staff{position:absolute;left:555px;top:240px;width:215px;height:215px;border-radius:100px 100px 16px 16px;
  background:linear-gradient(180deg,#fde6dc 0%,#f6c7d4 50%,#9dc9de 100%)}
.tagline{position:absolute;left:600px;top:160px;width:96px;height:60px;border:2px solid var(--pink);border-radius:30px;
  display:flex;align-items:center;justify-content:center;font-size:20px;font-weight:700;color:var(--pink);background:#fff}
.brand{position:absolute;left:85px;top:68px}
.brand-sub{font-size:24px;font-weight:700;color:var(--teal);letter-spacing:3px}
.brand-name{font-size:58px;font-weight:800;color:var(--teal);letter-spacing:4px;margin-top:2px;line-height:1.15}

.intro{position:absolute;top:478px;left:60px;width:730px;display:flex;justify-content:space-between}
.intro-block{width:340px}
.section-title{display:flex;align-items:center;gap:10px;font-size:19px;font-weight:700;color:var(--pink);
  padding-bottom:6px;border-bottom:2px dotted var(--sky-line);margin-bottom:16px}
.dot{width:22px;height:22px;border-radius:50%;background:var(--green);flex:none}
.intro-text{font-size:15px;line-height:1.75}
.care-list{list-style:none;font-size:15px;line-height:1.8}
.care-list li::before{content:"●";color:var(--teal);margin-right:4px;font-size:12px}

.flow-title{position:absolute;left:60px;top:690px;display:flex;align-items:center;gap:10px}
.flow-title svg{flex:none}
.flow-title span{font-size:22px;font-weight:700;color:var(--teal);line-height:1.3}
.flow-art{position:absolute;left:60px;top:780px;width:300px;height:235px;border-radius:12px;
  background:linear-gradient(180deg,#fbe7ee 0%,#f1e2d8 60%,#e6f1f6 100%)}

.steps{position:absolute;left:388px;top:705px;width:410px;list-style:none}
.step{display:flex;align-items:stretch;border:2px solid var(--sky-line);border-radius:8px;background:#fff;margin-bottom:18px;position:relative;min-height:58px}
.step:not(:last-child)::after{content:"";position:absolute;left:48px;bottom:-17px;border-left:10px solid transparent;border-right:10px solid transparent;border-top:12px solid var(--pink)}
.step-label{width:112px;flex:none;background:var(--pink-soft);display:flex;flex-direction:column;align-items:center;justify-content:center;border-right:2px solid var(--sky-line);padding:6px 4px;border-radius:6px 0 0 6px}
.step-num{width:22px;height:22px;border-radius:50%;background:var(--teal);color:#fff;font-size:13px;font-weight:700;display:flex;align-items:center;justify-content:center;margin-bottom:3px}
.step-name{font-size:13px;font-weight:700;color:var(--teal-dark)}
.step-text{font-size:12px;line-height:1.6;padding:7px 10px;display:flex;align-items:center}

.footer-town{position:absolute;left:0;bottom:0;width:849px;height:70px;
  background:linear-gradient(180deg,#eaf6fa 0%,#cfeaf2 100%)}
</style>
</head>
<body>

<header class="hero">
  <div class="hero-trees" role="img" aria-label="若葉の木々"></div>
  <div class="hero-land" role="img" aria-label="虹と緑の丘の風景"></div>
  <div class="hero-van" role="img" aria-label="医院名入りの送迎車"></div>
  <div class="hero-staff" role="img" aria-label="歯科医師と歯科衛生士の二人"></div>
  <p class="tagline">行きます</p>
  <div class="brand">
    <p class="brand-sub">訪問・送迎歯科クリニック</p>
    <h1 class="brand-name">RPE歯科医院</h1>
  </div>
</header>

<section class="intro">
  <div class="intro-block">
    <h2 class="section-title"><span class="dot"></span>訪問歯科診療とは</h2>
    <p class="intro-text">介護施設のご自宅で寝たきりの方や歩行が困難で通院ができない方のもとへ歯科医師や歯科衛生士が訪問し、診療を行う医療サービスです。</p>
  </div>
  <div class="intro-block">
    <h2 class="section-title"><span class="dot"></span>治療内容</h2>
    <ul class="care-list">
      <li>虫歯、歯周病の治療、予防</li>
      <li>入れ歯の作製、修理、調整</li>
      <li>口腔ケア・摂食嚥下指導</li>
      <li>お口のトラブル</li>
    </ul>
  </div>
</section>

<div class="flow-title">
  <svg width="40" height="44" viewBox="0 0 40 44" aria-hidden="true">
    <path d="M8 4c-6 2-7 12-4 20 2 6 3 16 7 16 3 0 3-10 9-10s6 10 9 10c4 0 5-10 7-16 3-8 2-18-4-20-5-2-8 2-12 2S13 2 8 4z" fill="none" stroke="var(--sky-line)" stroke-width="2.5"/>
  </svg>
  <span>訪問診療<br>の流れ</span>
</div>
<div class="flow-art" role="img" aria-label="ベッドで横になる患者さんに寄り添う歯科衛生士"></div>

<ol class="steps">
  <li class="step"><div class="step-label"><span class="step-num">1</span><span class="step-name">お申し込み</span></div>
    <p class="step-text">お電話・FAXなどでお気軽にお申込みください。</p></li>
  <li class="step"><div class="step-label"><span class="step-num">2</span><span class="step-name">訪問日の調整</span></div>
    <p class="step-text">ご希望に合わせて訪問日を決定します。</p></li>
  <li class="step"><div class="step-label"><span class="step-num">3</span><span class="step-name">無料検診</span></div>
    <p class="step-text">お口の状態を診察します。費用は一切かかりません。</p></li>
  <li class="step"><div class="step-label"><span class="step-num">4</span><span class="step-name">治　療</span></div>
    <p class="step-text">訪問診療を開始します。<br>初診時・月初めは、保険証等が必要になります。<br>1回の診療時間は30分程度です。</p></li>
  <li class="step"><div class="step-label"><span class="step-num">5</span><span class="step-name">今後のご相談</span></div>
    <p class="step-text">定期検診やブラッシング等のアフターケアのために定期的にお伺いします。<br>定期検診の時期はご相談の上で決めます。</p></li>
</ol>

<div class="footer-town" role="img" aria-label="水色の街並みのシルエット"></div>

</body>
</html>
```